Conservative, Modern and Sharp Builder Business card

Hi there,
We would like to update our existing business card.
I have attached photos of existing business card, logo and van sign.

I would like the business card to also list what we do :
Renovation • New Build • Alteration
Extension • Bathroom • Maintenance.(Seperated by dots)

Contact number : 021 0483 0752
(With that exact spacing)

Ideally when people looking from about 2-3 metres, they know that it is a builder’s business card

Open to suggestions on fonts, layout, style of business card

PLEASE ONLY SUBMIT YOUR BEST OR MAX 3 DESIGNS FOR EACH DESIGNER

Thanks

Industry/Entity Type

Construction. Renovation

Contact Information for Business Card

Details should be the same as the existing card. And addition of what we do.

Requirements
Should not have
• The new business card must not have the same layout as our existing one. Thanks

```html
<!DOCTYPE html>
<html lang="en">
<head>
<meta charset="utf-8">
<title>KeelBuild Business Card</title>
<link rel="stylesheet" href="https://fonts.googleapis.com/css2?family=Open+Sans:wght@400;700;800&display=swap">
<style>
  :root {
    --page-bg: #4a4a4a;
    --card-white: #f7f7f5;
    --card-black: #1b1b1b;
    --ink: #1e1e1e;
    --ink-soft: #555555;
    --divider: #c9c9c9;
    --reverse-ink: #f2f2f2;
  }
  * { box-sizing: border-box; margin: 0; padding: 0; }
  html, body {
    width: 1200px; height: 1112px; overflow: hidden;
    background: var(--page-bg);
    font-family: "Open Sans", Arial, sans-serif;
  }
  .sheet {
    width: 1200px; height: 1112px;
    display: flex; flex-direction: column; align-items: center; justify-content: center;
    gap: 40px;
  }
  .card {
    width: 860px; height: 492px; border-radius: 4px;
    box-shadow: 0 10px 28px rgba(0,0,0,.35);
    position: relative;
  }
  /* Front */
  .card-front {
    background: var(--card-white); color: var(--ink);
    display: flex; align-items: center;
  }
  .brand-block {
    width: 420px; display: flex; justify-content: center; align-items: center; gap: 14px;
  }
  .wordmark {
    font-weight: 800; font-size: 54px; letter-spacing: -0.5px; line-height: 1;
  }
  .brand-square { width: 14px; height: 14px; background: currentColor; }
  .divider { width: 1px; height: 250px; background: var(--divider); }
  .contact-block { padding-left: 44px; }
  .person-name { font-weight: 700; font-size: 30px; letter-spacing: 0.5px; }
  .person-role { font-size: 18px; color: var(--ink-soft); margin-bottom: 34px; }
  .contact-list { list-style: none; display: flex; flex-direction: column; gap: 8px; }
  .contact-list li { display: flex; align-items: center; gap: 12px; font-size: 20px; }
  .contact-list svg { width: 18px; height: 18px; flex: none; fill: var(--ink); }
  /* Back */
  .card-back {
    background: var(--card-black); color: var(--reverse-ink);
    display: flex; flex-direction: column; align-items: center; justify-content: center; gap: 40px;
  }
  .card-back .wordmark { font-size: 86px; }
  .card-back .brand-square { width: 20px; height: 20px; }
  .card-back .brand-block { width: auto; gap: 20px; }
  .services { text-align: center; font-size: 25px; line-height: 1.45; letter-spacing: 0.3px; }
  .sep {
    display: inline-grid; grid-template-columns: 5px 5px; gap: 2px;
    vertical-align: middle; margin: 0 10px;
  }
  .sep i { width: 5px; height: 5px; background: currentColor; display: block; }
</style>
</head>
<body>
<main class="sheet">
  <section class="card card-front">
    <div class="brand-block">
      <span class="brand-square"></span>
      <span class="wordmark">KeelBuild</span>
    </div>
    <div class="divider"></div>
    <div class="contact-block">
      <p class="person-name">Marko Tennant</p>
      <p class="person-role">Residential Builder</p>
      <ul class="contact-list">
        <li><svg viewBox="0 0 24 24" aria-hidden="true"><path d="M6.6 10.8a15 15 0 0 0 6.6 6.6l2.2-2.2a1 1 0 0 1 1-.25 11 11 0 0 0 3.6.6 1 1 0 0 1 1 1V20a1 1 0 0 1-1 1A17 17 0 0 1 3 4a1 1 0 0 1 1-1h3.5a1 1 0 0 1 1 1 11 11 0 0 0 .6 3.6 1 1 0 0 1-.25 1z"/></svg>021 0483 0752</li>
        <li><svg viewBox="0 0 24 24" aria-hidden="true"><path d="M2 5h20v14H2z M3.5 6.5 12 12.5l8.5-6z" fill-rule="evenodd"/></svg>KeelBuild@mailbox.com</li>
        <li><svg viewBox="0 0 24 24" aria-hidden="true"><path d="M12 2a10 10 0 1 0 0 20 10 10 0 0 0 0-20zm0 2c1.2 1.4 2 3.6 2.2 7H9.8C10 7.6 10.8 5.4 12 4zM9.8 13h4.4c-.2 3.4-1 5.6-2.2 7-1.2-1.4-2-3.6-2.2-7zM4.1 11a8 8 0 0 1 4.3-6.1A15 15 0 0 0 7.8 11zm0 2h3.7a15 15 0 0 0 .6 6.1A8 8 0 0 1 4.1 13zm12.1 0h3.7a8 8 0 0 1-4.3 6.1 15 15 0 0 0 .6-6.1zm0-2a15 15 0 0 0-.6-6.1A8 8 0 0 1 19.9 11z"/></svg>www.KeelBuild.nz</li>
        <li><svg viewBox="0 0 24 24" aria-hidden="true"><circle cx="12" cy="12" r="9"/></svg>KeelBuild.nz</li>
      </ul>
    </div>
  </section>

  <section class="card card-back">
    <div class="brand-block">
      <span class="brand-square"></span>
      <span class="wordmark">KeelBuild</span>
    </div>
    <p class="services">
      Renovation<span class="sep"><i></i><i></i><i></i><i></i></span>New Build<span class="sep"><i></i><i></i><i></i><i></i></span>Alteration<br>
      Extension<span class="sep"><i></i><i></i><i></i><i></i></span>Bathroom<span class="sep"><i></i><i></i><i></i><i></i></span>Maintenance.
    </p>
  </section>
</main>
</body>
</html>
```